Marine & Offshore company business card

We need a new logo design for a new company based in Singapore called "Bovenco Global Pte. Ltd.". We are suppliers of electrical items to marine and offshore industry. We specialise in lightings, cables terminations and junction box customisation. We would like the name card to have simple modern classic look.

Target Market(s)

my target customers are ship owners, shipyard purchasers, offshore purchasers.

Industry/Entity Type

Electrical

Font styles to use
Serif
Sans Serif

Colors

Designer to choose colors to be used in the design.

```html
<!DOCTYPE html>
<html lang="en">
<head>
<meta charset="utf-8">
<title>Bovenco Global – Business Card</title>
<link rel="stylesheet" href="https://fonts.googleapis.com/css2?family=Open+Sans:wght@400;600;700&display=swap">
<style>
  :root {
    --backdrop: #e0e0e0;
    --card-light: #ffffff;
    --card-dark: #333332;
    --ink: #333333;
    --gold: #c9a42c;
    --paper-text: #ffffff;
    --crop: #444444;
  }
  * { margin: 0; padding: 0; box-sizing: border-box; }
  html, body {
    width: 1200px; height: 1000px; overflow: hidden;
    background: var(--backdrop);
    font-family: "Open Sans", sans-serif;
  }
  .sheet { position: relative; width: 1200px; height: 1000px; }
  .crop-marks { position: absolute; inset: 0; }
  .card {
    position: absolute; left: 305px; width: 590px; height: 355px;
  }
  .card-front { top: 92px; background: var(--card-light); }
  .card-back { top: 572px; background: var(--card-dark); color: var(--paper-text); }

  .brand {
    position: absolute; display: flex; align-items: center; white-space: nowrap;
  }
  .brand-dot { border-radius: 50%; background: var(--gold); flex: none; }
  .brand-name { font-weight: 600; }

  .card-front .brand { left: 0; right: 0; top: 152px; justify-content: center; gap: 14px; }
  .card-front .brand-dot { width: 44px; height: 44px; }
  .card-front .brand-name { font-size: 27px; color: var(--ink); }

  .card-back .brand { left: 323px; top: 88px; gap: 10px; }
  .card-back .brand-dot { width: 30px; height: 30px; }
  .card-back .brand-name { font-size: 17px; color: var(--paper-text); }

  .holder { position: absolute; left: 55px; top: 122px; }
  .holder-name { font-size: 19px; font-weight: 700; line-height: 24px; }
  .holder-role { font-size: 14px; line-height: 18px; }

  .company { position: absolute; left: 55px; top: 190px; font-size: 12.5px; line-height: 14.5px; }
  .company-name { font-size: 14px; font-weight: 700; line-height: 18px; }

  .phones { position: absolute; left: 55px; top: 266px; font-size: 12.5px; line-height: 14.5px; }
  .phones dt { float: left; width: 39px; clear: left; }
  .phones dd { margin-left: 39px; }

  .online { position: absolute; left: 255px; top: 279px; font-size: 12.5px; font-weight: 700; line-height: 15px; }
</style>
</head>
<body>
<div class="sheet">
  <svg class="crop-marks" width="1200" height="1000" viewBox="0 0 1200 1000" aria-hidden="true">
    <g stroke="var(--crop)" stroke-width="1">
      <line x1="334.5" y1="53" x2="334.5" y2="108"/><line x1="866.5" y1="53" x2="866.5" y2="108"/>
      <line x1="334.5" y1="431" x2="334.5" y2="487"/><line x1="866.5" y1="431" x2="866.5" y2="487"/>
      <line x1="266" y1="122.5" x2="321" y2="122.5"/><line x1="878" y1="122.5" x2="934" y2="122.5"/>
      <line x1="266" y1="417.5" x2="321" y2="417.5"/><line x1="878" y1="417.5" x2="934" y2="417.5"/>
      <line x1="334.5" y1="533" x2="334.5" y2="588"/><line x1="866.5" y1="533" x2="866.5" y2="588"/>
      <line x1="334.5" y1="911" x2="334.5" y2="966"/><line x1="866.5" y1="911" x2="866.5" y2="966"/>
      <line x1="266" y1="602.5" x2="321" y2="602.5"/><line x1="878" y1="602.5" x2="934" y2="602.5"/>
      <line x1="266" y1="897.5" x2="321" y2="897.5"/><line x1="878" y1="897.5" x2="934" y2="897.5"/>
    </g>
  </svg>

  <section class="card card-front">
    <div class="brand">
      <span class="brand-dot"></span>
      <span class="brand-name">Bovenco Global Pte. Ltd.</span>
    </div>
  </section>

  <section class="card card-back">
    <div class="brand">
      <span class="brand-dot"></span>
      <span class="brand-name">Bovenco Global Pte. Ltd.</span>
    </div>

    <div class="holder">
      <p class="holder-name">Name Surname</p>
      <p class="holder-role">Position</p>
    </div>

    <address class="company" style="font-style:normal">
      <p class="company-name">Bovenco Global PTE LTD</p>
      <p>Bulding Name, Office 123</p>
      <p>Something Avenue 456</p>
      <p>ST-7890 Singapore</p>
    </address>

    <dl class="phones">
      <dt>Tel:</dt><dd>+65 1234 5678</dd>
      <dt>Fax:</dt><dd>+65 1234 5679</dd>
      <dt>Mob:</dt><dd>+9&nbsp;&nbsp;&nbsp;1234 4321</dd>
    </dl>

    <div class="online">
      <p>www.bovencoglobal.com</p>
      <p>n.surname@bovencoglobal.com</p>
    </div>
  </section>
</div>
</body>
</html>
```